TKA Electricial Contracting Services

Hi guys, after a design for my small electrical company, have logo design files to be incorporated into the layout, the basic concept is electrical contracting services for residential, commercial, industrial & data services, image is clean clear and strong,

Card format is to have a nice clean logo on front,with maybe the Residential – commercial – industrial - data, followed with licensed & insured, followed by contact details on backside of the card.

Target Market(s)

Residential, commercial, industrial sectors.

Industry/Entity Type

Electrical

Contact Information for Business Card

TKA logo,
Residential – commercial – industrial - data
REC: 61372
Email: tka@poralink.net.au
Phone: 0458 203 719

Requirements
Must have
• Clean & strong design.
Nice to have
• If possible, I would like the logo colours inverted so the text is orange and the background is black on the front of the card, then the backside of the card be the reverse colour
Should not have
• No Sparks, lightning bolts,

```html
<!DOCTYPE html>
<html lang="en">
<head>
<meta charset="utf-8">
<title>TKA Electrical – Business Card</title>
<link rel="stylesheet" href="https://fonts.googleapis.com/css2?family=Exo+2:wght@500;700;800&display=swap">
<style>
  :root {
    --backdrop: #2e2926;
    --card-black: #151414;
    --orange: #f07e16;
    --white: #ffffff;
    --rule: #5a5550;
  }
  * { box-sizing: border-box; margin: 0; padding: 0; }
  html, body {
    width: 1200px; height: 716px; overflow: hidden;
    background: var(--backdrop);
    font-family: "Exo 2", sans-serif;
  }
  .canvas { position: relative; width: 1200px; height: 716px; }

  .card {
    position: absolute; top: 215px;
    width: 500px; height: 286px;
    border-radius: 6px; overflow: hidden;
    box-shadow: 0 12px 30px rgba(0,0,0,.45);
  }

  /* Front */
  .card-front { left: 70px; background: var(--card-black); }
  .front-brand {
    position: absolute; left: 60px; top: 52px;
    width: 380px;
  }
  .brand-mark {
    display: flex; align-items: flex-end; gap: 14px;
  }
  .brand-name {
    font-weight: 800; font-size: 104px; line-height: .9;
    color: var(--orange); letter-spacing: -2px;
  }
  .front-phone {
    writing-mode: vertical-rl; transform: rotate(180deg);
    color: var(--orange); font-weight: 700; font-size: 15px;
    letter-spacing: 1px; margin-bottom: 4px;
  }
  .company-name {
    margin-top: 8px;
    color: var(--orange); font-weight: 700; font-size: 25px;
    letter-spacing: .5px;
  }
  .front-rule {
    height: 1px; background: var(--rule); margin: 8px 0 7px;
  }
  .services {
    color: var(--orange); font-weight: 500; font-size: 14px;
    letter-spacing: .6px; white-space: nowrap;
  }

  /* Back */
  .card-back { left: 630px; background: var(--card-black); }
  .back-tab {
    position: absolute; left: 12px; top: 96px;
    width: 8px; height: 94px; border-radius: 4px;
    background: var(--orange);
  }
  .back-brand {
    position: absolute; left: 36px; top: 38px;
    width: 190px; height: 210px;
    display: flex; align-items: center; justify-content: center;
  }
  .back-brand-inner {
    transform: rotate(-90deg);
    width: 210px;
  }
  .back-brand .brand-name {
    color: var(--white); font-size: 64px; letter-spacing: -1px;
  }
  .back-brand .company-name {
    color: var(--white); font-size: 15px; margin-top: 4px;
  }
  .back-brand .front-rule { margin: 5px 0 4px; }
  .back-brand .services {
    font-size: 13px; white-space: normal; line-height: 1.25;
  }

  .back-panel {
    position: absolute; right: 0; top: 0;
    width: 272px; height: 286px;
    background: var(--orange);
    padding: 44px 22px 0 26px;
    color: var(--card-black);
  }
  .back-notch {
    position: absolute; left: 228px; top: 52px;
    width: 10px; height: 180px;
    background: var(--card-black);
    border-radius: 0 6px 6px 0;
  }
  .rec-number { font-weight: 700; font-size: 17px; margin-bottom: 16px; }
  .service-list {
    font-weight: 700; font-size: 16px; line-height: 1.18;
    margin-bottom: 14px;
  }
  .contact-line {
    display: flex; align-items: center; gap: 8px;
    font-weight: 700;
  }
  .contact-email { font-size: 14px; font-weight: 500; }
  .contact-phone { font-size: 18px; margin-top: 2px; }
  .contact-icon { width: 12px; height: 12px; flex: none; }
</style>
</head>
<body>
<main class="canvas">

  <section class="card card-front" aria-label="Card front">
    <div class="front-brand">
      <div class="brand-mark">
        <span class="brand-name">TKA</span>
        <span class="front-phone">0458 203 719</span>
      </div>
      <p class="company-name">Tyler Kane Electrical</p>
      <div class="front-rule"></div>
      <p class="services">Residential - Commercial - Industrial - Data</p>
    </div>
  </section>

  <section class="card card-back" aria-label="Card back">
    <div class="back-tab"></div>
    <div class="back-brand">
      <div class="back-brand-inner">
        <span class="brand-name">TKA</span>
        <p class="company-name">Tyler Kane Electrical</p>
        <div class="front-rule"></div>
        <p class="services">Residential - Commercial<br>Industrial - Data</p>
      </div>
    </div>
    <div class="back-panel">
      <p class="rec-number">REC: 61372</p>
      <p class="service-list">New installations Additions<br>Rewiring Repairs<br>Maintenance 24 hours<br>Faults and Emergency<br>Assistance</p>
      <p class="contact-line contact-email">
        <svg class="contact-icon" viewBox="0 0 12 12" aria-hidden="true">
          <rect x="1" y="2.5" width="10" height="7" fill="none" stroke="#151414" stroke-width="1.2"/>
          <path d="M1 2.5 L6 6.5 L11 2.5" fill="none" stroke="#151414" stroke-width="1.2"/>
        </svg>
        tka@poralink.net.au
      </p>
      <p class="contact-line contact-phone">
        <svg class="contact-icon" viewBox="0 0 12 12" aria-hidden="true">
          <rect x="3" y="0.5" width="6" height="11" rx="1.2" fill="#151414"/>
          <rect x="4" y="1.8" width="4" height="7" fill="#f07e16"/>
        </svg>
        0458 203 719
      </p>
    </div>
  </section>

</main>
</body>
</html>
```